100% Organic Beard Care Product labels

We need labels for our organic beard care products, this includes 30ml matt black bottles, 50ml matt black jars and 100ml matt black boston bottles.
We have six beard oil products, three beard balm products, and one beard shampoo.
Would like white on black, or white on transparent print and logo.
Logo is attached along with an idea of label for our unscented product.

Target Market(s)

Mens beard care

Font styles to use
Other font styles liked:
• Verdana

```html
<!DOCTYPE html>
<html lang="en">
<head>
<meta charset="utf-8">
<title>Kingsmoor Men – Organic Beard Care Labels</title>
<link rel="stylesheet" href="https://fonts.googleapis.com/css2?family=Arimo:ital,wght@0,400;0,700;1,400&family=Open+Sans:wght@400;700&display=swap">
<style>
  :root {
    --label-black: #000000;
    --ink-white: #ffffff;
    --sheet: #ffffff;
  }
  * { box-sizing: border-box; margin: 0; padding: 0; }
  html, body { width: 1200px; height: 874px; overflow: hidden; background: var(--sheet); }
  .sheet { position: relative; width: 1200px; height: 874px; }

  .label {
    position: absolute;
    width: 355px;
    height: 250px;
    background: var(--label-black);
    color: var(--ink-white);
    font-family: "Arimo", Verdana, sans-serif;
  }
  .label::before {
    content: "";
    position: absolute;
    inset: 4px;
    border: 1.5px solid var(--ink-white);
  }

  .brand {
    position: absolute;
    left: 0; right: 0; top: 18px;
    display: flex;
    flex-direction: column;
    align-items: center;
  }
  .brand-dot {
    width: 52px; height: 52px;
    border-radius: 50%;
    background: var(--ink-white);
  }
  .brand-name {
    margin-top: 8px;
    font-size: 15px;
    font-weight: 700;
    line-height: 16px;
    text-align: center;
    letter-spacing: 0.5px;
  }

  .product {
    position: absolute;
    left: 0; right: 0; top: 142px;
    text-align: center;
  }
  .product-title {
    display: inline-block;
    font-size: 22px;
    letter-spacing: 1px;
    line-height: 24px;
    padding: 0 2px 1px;
    border-bottom: 1px solid var(--ink-white);
  }
  .product-claim {
    font-size: 15px;
    font-style: italic;
    line-height: 20px;
    margin-top: 1px;
  }
  .product-scent {
    font-size: 13px;
    line-height: 16px;
    margin-top: 14px;
  }
  .product-size {
    font-size: 13px;
    line-height: 16px;
  }

  .side-text {
    position: absolute;
    writing-mode: vertical-rl;
    transform: rotate(180deg);
    font-family: "Open Sans", Verdana, sans-serif;
    font-size: 5.6px;
    line-height: 7.4px;
  }
  .side-text strong { font-weight: 700; }
  .maker { left: 16px; top: 14px; height: 64px; text-align: end; }
  .how-to { left: 16px; bottom: 14px; height: 120px; }
  .ingredients { left: 297px; bottom: 14px; height: 222px; }

  .shelf-life {
    position: absolute;
    left: 18px; top: 82px;
    width: 10px; height: 14px;
  }
</style>
</head>
<body>
<main class="sheet">

  <!-- Row: beard oil -->
  <section class="label" style="left:30px; top:30px;">
    <div class="side-text maker">kingsmoormen.co.uk<br>Kingsmoor Men<br>NR3 5QT</div>
    <svg class="shelf-life" viewBox="0 0 10 14" aria-label="Use within 12 months"><rect x="1" y="1" width="8" height="12" fill="none" stroke="#fff" stroke-width="1"/></svg>
    <div class="side-text how-to"><strong>HOW TO USE</strong><br>Drop a small amount of oil onto the palm<br>of your hand. Rub hands together then<br>work the oil into the facial hair.</div>
    <div class="side-text ingredients"><strong>INGREDIENTS</strong><br>Organic Grapeseed Oil (Vitis vinifera), Organic Sweet Almond Oil<br>(Prunus dulcis), Organic Jojoba (Simmondsia chinesis), Organic<br>Caster Oil (Ricinus Communis Seed Oil), Organic Argan Oil<br>(Argania Spinosa)</div>
    <div class="brand"><span class="brand-dot"></span><span class="brand-name">KINGSMOOR<br>MEN</span></div>
    <div class="product"><span class="product-title">BEARD OIL</span><p class="product-claim">100% Organic</p><p class="product-scent">Unscented</p><p class="product-size">30ml</p></div>
  </section>

  <section class="label" style="left:421px; top:30px;">
    <div class="side-text maker">kingsmoormen.co.uk<br>Kingsmoor Men<br>NR3 5QT</div>
    <svg class="shelf-life" viewBox="0 0 10 14" aria-label="Use within 12 months"><rect x="1" y="1" width="8" height="12" fill="none" stroke="#fff" stroke-width="1"/></svg>
    <div class="side-text how-to"><strong>HOW TO USE</strong><br>Drop a small amount of oil onto the palm<br>of your hand. Rub hands together then<br>work the oil into the facial hair.</div>
    <div class="side-text ingredients"><strong>INGREDIENTS</strong><br>Organic Grapeseed Oil (Vitis vinifera), Organic Sweet Almond Oil<br>(Prunus dulcis), Organic Jojoba (Simmondsia chinesis), Organic<br>Caster Oil (Ricinus Communis Seed Oil), Organic Argan Oil<br>(Argania Spinosa)</div>
    <div class="brand"><span class="brand-dot"></span><span class="brand-name">KINGSMOOR<br>MEN</span></div>
    <div class="product"><span class="product-title">BEARD OIL</span><p class="product-claim">100% Organic</p><p class="product-scent">Unscented</p><p class="product-size">50ml</p></div>
  </section>

  <section class="label" style="left:810px; top:30px;">
    <div class="side-text maker">kingsmoormen.co.uk<br>Kingsmoor Men<br>NR3 5QT</div>
    <svg class="shelf-life" viewBox="0 0 10 14" aria-label="Use within 12 months"><rect x="1" y="1" width="8" height="12" fill="none" stroke="#fff" stroke-width="1"/></svg>
    <div class="side-text how-to"><strong>HOW TO USE</strong><br>Drop a small amount of oil onto the palm<br>of your hand. Rub hands together then<br>work the oil into the facial hair.</div>
    <div class="side-text ingredients"><strong>INGREDIENTS</strong><br>Organic Grapeseed Oil (Vitis vinifera), Organic Sweet Almond Oil<br>(Prunus dulcis), Organic Jojoba (Simmondsia chinesis), Organic<br>Caster Oil (Ricinus Communis Seed Oil), Organic Argan Oil<br>(Argania Spinosa)</div>
    <div class="brand"><span class="brand-dot"></span><span class="brand-name">KINGSMOOR<br>MEN</span></div>
    <div class="product"><span class="product-title">BEARD OIL</span><p class="product-claim">100% Organic</p><p class="product-scent">Unscented</p><p class="product-size">100ml</p></div>
  </section>

  <!-- Row: beard shampoo -->
  <section class="label" style="left:30px; top:315px;">
    <div class="side-text maker">kingsmoormen.co.uk<br>Kingsmoor Men<br>NR3 5QT</div>
    <svg class="shelf-life" viewBox="0 0 10 14" aria-label="Use within 12 months"><rect x="1" y="1" width="8" height="12" fill="none" stroke="#fff" stroke-width="1"/></svg>
    <div class="side-text how-to"><strong>HOW TO USE</strong><br>Drop a small amount of oil onto the palm<br>of your hand. Rub hands together then<br>work the oil into the facial hair.</div>
    <div class="side-text ingredients"><strong>INGREDIENTS</strong><br>Organic Grapeseed Oil (Vitis vinifera), Organic Sweet Almond Oil<br>(Prunus dulcis), Organic Jojoba (Simmondsia chinesis), Organic<br>Caster Oil (Ricinus Communis Seed Oil), Organic Argan Oil<br>(Argania Spinosa)</div>
    <div class="brand"><span class="brand-dot"></span><span class="brand-name">KINGSMOOR<br>MEN</span></div>
    <div class="product"><span class="product-title">BEARD SHAMPOO</span><p class="product-claim">100% Organic</p><p class="product-scent">Unscented</p><p class="product-size">30ml</p></div>
  </section>

  <section class="label" style="left:425px; top:315px;">
    <div class="side-text maker">kingsmoormen.co.uk<br>Kingsmoor Men<br>NR3 5QT</div>
    <svg class="shelf-life" viewBox="0 0 10 14" aria-label="Use within 12 months"><rect x="1" y="1" width="8" height="12" fill="none" stroke="#fff" stroke-width="1"/></svg>
    <div class="side-text how-to"><strong>HOW TO USE</strong><br>Drop a small amount of oil onto the palm<br>of your hand. Rub hands together then<br>work the oil into the facial hair.</div>
    <div class="side-text ingredients"><strong>INGREDIENTS</strong><br>Organic Grapeseed Oil (Vitis vinifera), Organic Sweet Almond Oil<br>(Prunus dulcis), Organic Jojoba (Simmondsia chinesis), Organic<br>Caster Oil (Ricinus Communis Seed Oil), Organic Argan Oil<br>(Argania Spinosa)</div>
    <div class="brand"><span class="brand-dot"></span><span class="brand-name">KINGSMOOR<br>MEN</span></div>
    <div class="product"><span class="product-title">BEARD SHAMPOO</span><p class="product-claim">100% Organic</p><p class="product-scent">Unscented</p><p class="product-size">50ml</p></div>
  </section>

  <section class="label" style="left:814px; top:315px;">
    <div class="side-text maker">kingsmoormen.co.uk<br>Kingsmoor Men<br>NR3 5QT</div>
    <svg class="shelf-life" viewBox="0 0 10 14" aria-label="Use within 12 months"><rect x="1" y="1" width="8" height="12" fill="none" stroke="#fff" stroke-width="1"/></svg>
    <div class="side-text how-to"><strong>HOW TO USE</strong><br>Drop a small amount of oil onto the palm<br>of your hand. Rub hands together then<br>work the oil into the facial hair.</div>
    <div class="side-text ingredients"><strong>INGREDIENTS</strong><br>Organic Grapeseed Oil (Vitis vinifera), Organic Sweet Almond Oil<br>(Prunus dulcis), Organic Jojoba (Simmondsia chinesis), Organic<br>Caster Oil (Ricinus Communis Seed Oil), Organic Argan Oil<br>(Argania Spinosa)</div>
    <div class="brand"><span class="brand-dot"></span><span class="brand-name">KINGSMOOR<br>MEN</span></div>
    <div class="product"><span class="product-title">BEARD SHAMPOO</span><p class="product-claim">100% Organic</p><p class="product-scent">Unscented</p><p class="product-size">100ml</p></div>
  </section>

  <!-- Row: beard balm -->
  <section class="label" style="left:30px; top:594px;">
    <div class="side-text maker">kingsmoormen.co.uk<br>Kingsmoor Men<br>NR3 5QT</div>
    <svg class="shelf-life" viewBox="0 0 10 14" aria-label="Use within 12 months"><rect x="1" y="1" width="8" height="12" fill="none" stroke="#fff" stroke-width="1"/></svg>
    <div class="side-text how-to"><strong>HOW TO USE</strong><br>Drop a small amount of oil onto the palm<br>of your hand. Rub hands together then<br>work the oil into the facial hair.</div>
    <div class="side-text ingredients"><strong>INGREDIENTS</strong><br>Organic Grapeseed Oil (Vitis vinifera), Organic Sweet Almond Oil<br>(Prunus dulcis), Organic Jojoba (Simmondsia chinesis), Organic<br>Caster Oil (Ricinus Communis Seed Oil), Organic Argan Oil<br>(Argania Spinosa)</div>
    <div class="brand"><span class="brand-dot"></span><span class="brand-name">KINGSMOOR<br>MEN</span></div>
    <div class="product"><span class="product-title">BEARD BALM</span><p class="product-claim">100% Organic</p><p class="product-scent">Unscented</p><p class="product-size">30ml</p></div>
  </section>

  <section class="label" style="left:425px; top:594px;">
    <div class="side-text maker">kingsmoormen.co.uk<br>Kingsmoor Men<br>NR3 5QT</div>
    <svg class="shelf-life" viewBox="0 0 10 14" aria-label="Use within 12 months"><rect x="1" y="1" width="8" height="12" fill="none" stroke="#fff" stroke-width="1"/></svg>
    <div class="side-text how-to"><strong>HOW TO USE</strong><br>Drop a small amount of oil onto the palm<br>of your hand. Rub hands together then<br>work the oil into the facial hair.</div>
    <div class="side-text ingredients"><strong>INGREDIENTS</strong><br>Organic Grapeseed Oil (Vitis vinifera), Organic Sweet Almond Oil<br>(Prunus dulcis), Organic Jojoba (Simmondsia chinesis), Organic<br>Caster Oil (Ricinus Communis Seed Oil), Organic Argan Oil<br>(Argania Spinosa)</div>
    <div class="brand"><span class="brand-dot"></span><span class="brand-name">KINGSMOOR<br>MEN</span></div>
    <div class="product"><span class="product-title">BEARD BALM</span><p class="product-claim">100% Organic</p><p class="product-scent">Unscented</p><p class="product-size">50ml</p></div>
  </section>

  <section class="label" style="left:814px; top:594px;">
    <div class="side-text maker">kingsmoormen.co.uk<br>Kingsmoor Men<br>NR3 5QT</div>
    <svg class="shelf-life" viewBox="0 0 10 14" aria-label="Use within 12 months"><rect x="1" y="1" width="8" height="12" fill="none" stroke="#fff" stroke-width="1"/></svg>
    <div class="side-text how-to"><strong>HOW TO USE</strong><br>Drop a small amount of oil onto the palm<br>of your hand. Rub hands together then<br>work the oil into the facial hair.</div>
    <div class="side-text ingredients"><strong>INGREDIENTS</strong><br>Organic Grapeseed Oil (Vitis vinifera), Organic Sweet Almond Oil<br>(Prunus dulcis), Organic Jojoba (Simmondsia chinesis), Organic<br>Caster Oil (Ricinus Communis Seed Oil), Organic Argan Oil<br>(Argania Spinosa)</div>
    <div class="brand"><span class="brand-dot"></span><span class="brand-name">KINGSMOOR<br>MEN</span></div>
    <div class="product"><span class="product-title">BEARD BALM</span><p class="product-claim">100% Organic</p><p class="product-scent">Unscented</p><p class="product-size">100ml</p></div>
  </section>

</main>
</body>
</html>
```